Tarn - Stationary Design/Layout

We are a well established clothing design and manufacturing company (Tarn Sourcing) based in London UK, with our own factory in Bangladesh, supplying to many fashion retailers and brands. Our factory has very high environmental and ethical standards with people at its heart. Our quality of garments are second to none.
Our new logo has been proudly developed by the Pixel Guild community last month, we are now in the second phase and need the layout designed for our letterheads, double sided business cards, compliment slip and clothing ticket. Feel as creative as you like, but make sure it looks great!!
***The Logo - the logo design and colour is set and should NOT be changed and stay on a dark grey backround. The logo artwork to use is attached.
***Details to use for the business card:
Dorian Pelham
Direct Line: 020 7946 0158
dorian@tarnsourcing-example.com
Tarn Sourching Ltd.
57 - 59 Hollin Row
Camdon . Swindon
NW9 4QT
Switchboard: 020 7946 0274
Fax: 020 7946 0274
www.tarnsourcing-example.co.uk
***Details to use for the letterhead and compliment slip:
Tarn Sourching Ltd.
57 - 59 Hollin Row
Camdon . Swindon
NW9 4QT
Fax: 020 7946 0274
www.tarnsourcing-example.co.uk
***Details for Swing Ticket:
Size: 12cm height by 5.5cm width
One side need to have just the logo without the 'Sourcing', on the other it needs to stay blank

```html
<!DOCTYPE html>
<html lang="en">
<head>
<meta charset="utf-8">
<title>Tarn Sourcing – Stationery</title>
<link rel="stylesheet" href="https://fonts.googleapis.com/css2?family=Arimo:wght@400&display=swap">
<style>
  :root {
    --backdrop: #6e5e4b;
    --paper: #ffffff;
    --band: #b9b9bb;
    --band-text: #f4f4f4;
    --address-text: #eeeeee;
    --logo-ground: #4b4846;
    --logo-ink: #9fd4d8;
    --edge: #d6d6d6;
  }
  * { box-sizing: border-box; margin: 0; padding: 0; }
  html, body { width: 1200px; height: 1200px; overflow: hidden; }
  body {
    position: relative;
    background: var(--backdrop);
    font-family: "Arimo", Arial, sans-serif;
  }
  .sheet {
    position: absolute;
    background: var(--paper);
    overflow: hidden;
  }
  .letterhead { left: 226px; top: 116px; width: 750px; height: 964px; }
  .compliment-slip {
    left: 279px; top: 382px; width: 826px; height: 359px;
    border: 1px solid var(--edge);
    box-shadow: 0 1px 3px rgba(0,0,0,0.18);
  }
  .logo-plate {
    position: absolute;
    left: 0;
    padding: 0 14px;
    background: var(--logo-ground);
    display: flex;
    align-items: center;
    justify-content: center;
  }
  .letterhead .logo-plate { top: 26px; width: 207px; height: 84px; }
  .compliment-slip .logo-plate { top: 26px; width: 205px; height: 87px; }
  .logo-name {
    color: var(--logo-ink);
    font-weight: 400;
    font-size: 18px;
    letter-spacing: 1.5px;
    text-transform: uppercase;
    white-space: nowrap;
  }
  .footer-band {
    position: absolute;
    left: 0; right: 0; bottom: 0;
    background: var(--band);
  }
  .letterhead .footer-band { height: 69px; }
  .compliment-slip .footer-band { height: 68px; }
  .web-address {
    position: absolute;
    top: 50%;
    transform: translate(-50%, -50%);
    color: var(--band-text);
    font-size: 11px;
    letter-spacing: 0.3px;
    white-space: nowrap;
  }
  .letterhead .web-address { left: 376px; }
  .compliment-slip .web-address { left: 413px; }
  .postal-address {
    position: absolute;
    right: 10px;
    top: 6px;
    color: var(--address-text);
    font-size: 6.5px;
    line-height: 8.6px;
    text-align: right;
    font-style: normal;
    white-space: nowrap;
  }
  .postal-address .gap { margin-top: 3px; }
</style>
</head>
<body>

  <section class="sheet letterhead" aria-label="Letterhead">
    <div class="logo-plate"><span class="logo-name">Tarn Sourcing</span></div>
    <footer class="footer-band">
      <span class="web-address">www.tarnsourcing-example.co.uk</span>
      <address class="postal-address">
        <div>Tarn Sourching Ltd.</div>
        <div>57 - 59 Hollin Row</div>
        <div class="gap">Camdon . Swindon</div>
        <div>NW9 4QT</div>
        <div class="gap">Switchboard: 020 7946 0274</div>
        <div>Fax: 020 7946 0274</div>
      </address>
    </footer>
  </section>

  <section class="sheet compliment-slip" aria-label="Compliment slip">
    <div class="logo-plate"><span class="logo-name">Tarn Sourcing</span></div>
    <footer class="footer-band">
      <span class="web-address">www.tarnsourcing-example.co.uk</span>
      <address class="postal-address">
        <div>Tarn Sourching Ltd.</div>
        <div>57 - 59 Hollin Row</div>
        <div class="gap">Camdon . Swindon</div>
        <div>NW9 4QT</div>
        <div class="gap">Switchboard: 020 7946 0274</div>
        <div>Fax: 020 7946 0274</div>
      </address>
    </footer>
  </section>

</body>
</html>
```